JT & WE Shearing Pty Ltd

We already have an existing logo created by Lumen Quarry however we have restructured to a company. We would like someone to add Pty Ltd to our business name please.

Colors

Designer to choose only greyscale colors for use in the design.

```html
<!DOCTYPE html>
<html lang="en">
<head>
<meta charset="utf-8">
<title>JT &amp; WE Shearing Pty Ltd – Business Cards</title>
<link href="https://fonts.googleapis.com/css2?family=Lato:wght@400;700;900&display=swap" rel="stylesheet">
<style>
  :root {
    --bg: #2a2a2a;
    --card: #ffffff;
    --ink: #111111;
    --rule: #9a9a9a;
    --shadow: rgba(0, 0, 0, 0.45);
  }
  * { margin: 0; padding: 0; box-sizing: border-box; }
  html, body {
    width: 1200px;
    height: 900px;
    overflow: hidden;
    background: var(--bg);
    font-family: "Lato", Arial, sans-serif;
    color: var(--ink);
  }
  .stage {
    position: relative;
    width: 1200px;
    height: 900px;
  }
  .card {
    position: absolute;
    left: 320px;
    width: 560px;
    height: 320px;
    background: var(--card);
    box-shadow: 0 14px 30px var(--shadow);
    display: flex;
    align-items: center;
  }
  .card--front { top: 100px; justify-content: center; }
  .card--back { top: 480px; padding: 0 40px 0 44px; }

  .brand {
    display: flex;
    align-items: center;
    gap: 12px;
  }
  .brand__dot {
    width: 22px;
    height: 22px;
    border-radius: 50%;
    background: var(--ink);
    flex: none;
  }
  .brand__name {
    font-weight: 900;
    font-size: 25px;
    line-height: 1.1;
    letter-spacing: 0.5px;
    color: var(--ink);
    text-transform: uppercase;
  }
  .card--back .brand__name { font-size: 21px; }
  .card--back .brand__dot { width: 18px; height: 18px; }

  .divider {
    width: 1px;
    height: 112px;
    background: var(--rule);
    margin: 0 22px 0 26px;
    flex: none;
  }
  .contact__name {
    font-weight: 900;
    font-size: 15px;
    letter-spacing: 0.6px;
    text-transform: uppercase;
    margin-bottom: 12px;
  }
  .contact__list { list-style: none; }
  .contact__item {
    display: flex;
    align-items: center;
    gap: 8px;
    font-size: 13.5px;
    margin-bottom: 7px;
  }
  .contact__item:last-child { margin-top: 8px; }
  .contact__icon { width: 18px; height: 18px; flex: none; }
</style>
</head>
<body>
<main class="stage">

  <section class="card card--front" aria-label="Card front">
    <div class="brand">
      <span class="brand__dot"></span>
      <span class="brand__name">JT &amp; WE Shearing<br>Pty Ltd</span>
    </div>
  </section>

  <section class="card card--back" aria-label="Card back">
    <div class="brand">
      <span class="brand__dot"></span>
      <span class="brand__name">JT &amp; WE Shearing<br>Pty Ltd</span>
    </div>
    <div class="divider"></div>
    <div class="contact">
      <p class="contact__name">Tom Callander</p>
      <ul class="contact__list">
        <li class="contact__item">
          <svg class="contact__icon" viewBox="0 0 18 18" aria-hidden="true">
            <circle cx="9" cy="9" r="9" fill="#111"/>
            <path d="M5.5 7.5h7v1.2c0 .5-.4.8-.9.8H6.4c-.5 0-.9-.3-.9-.8z M6.5 10h5l.6 2.5H5.9z" fill="#fff"/>
            <rect x="8" y="6" width="2" height="1.5" fill="#fff"/>
          </svg>
          <span>044 7150292</span>
        </li>
        <li class="contact__item">
          <svg class="contact__icon" viewBox="0 0 18 18" aria-hidden="true">
            <circle cx="9" cy="9" r="9" fill="#111"/>
            <rect x="4.5" y="6" width="9" height="6.5" fill="none" stroke="#fff" stroke-width="1.1"/>
            <path d="M4.5 6l4.5 3.8L13.5 6" fill="none" stroke="#fff" stroke-width="1.1"/>
          </svg>
          <span>jtweshearing@mailbox.net</span>
        </li>
        <li class="contact__item">
          <svg class="contact__icon" viewBox="0 0 18 18" aria-hidden="true">
            <circle cx="9" cy="9" r="9" fill="#111"/>
            <path d="M9 3.8a3.4 3.4 0 0 0-3.4 3.4c0 2.5 3.4 6.3 3.4 6.3s3.4-3.8 3.4-6.3A3.4 3.4 0 0 0 9 3.8z" fill="#fff"/>
            <circle cx="9" cy="7.2" r="1.3" fill="#111"/>
          </svg>
          <span>PO Box 418 Dunmore WA 6402</span>
        </li>
      </ul>
    </div>
  </section>

</main>
</body>
</html>
```